Industry: Christian Ministry using Magic, Music and Multimedia to teach gospel

“Lanternfold Ministries brings the Gospel of Jesus Christ, with heart-seeking, biblical accuracy
through live, entertainment-based evangelistic Celebrations."

We are a service that wants to partner with christian religious institutions and churches to teach biblical gospel in a fun and entertaining way using magic.

Design inspiration: https://www.quillmarshwonders.example

DO NOT CONTACT ME PRIVATELY. IT WILL BE IGNORED.

Important:
1. Use only royalty free graphics
2. Use only google fonts
3. A clean, linear layout
4. Do not include search

PAGES

1. Home
2. Shows & Skylark
3. About Lanternfold
4. Media
5. Contact & Support

Color pallets
#0053E0
#FF2500
#ffffff

Please see attachment for more detail

Target Market(s)

Churches and christian schools

Industry/Entity Type

magic, entertainment, christianity

Number of Pages Required

5+ page

Colors
0054AA
0677BA
7BADD7
CADEEF
E8F1F8

Requirements
Should not have
• - search bar

```html
<!DOCTYPE html>
<html lang="en">
<head>
<meta charset="utf-8">
<title>Lanternfold Ministries</title>
<link rel="stylesheet" href="https://fonts.googleapis.com/css2?family=Merriweather:ital,wght@0,400;0,700;0,900;1,400&family=Lato:ital,wght@0,400;0,700;1,400&display=swap">
<style>
:root{
  --blue:#0053E0;
  --blue-deep:#0a3fc4;
  --red:#FF2500;
  --red-deep:#e61c00;
  --white:#ffffff;
  --ink:#111111;
  --body:#333333;
  --footer:#0d0d0d;
}
*{box-sizing:border-box;margin:0;padding:0}
html,body{width:1200px;height:4658px;overflow:hidden}
body{font-family:"Lato",sans-serif;color:var(--body);background:var(--white);position:relative}

.hero{position:absolute;left:0;top:0;width:1200px;height:596px;
  background:
    radial-gradient(ellipse 380px 260px at 50% 72%,rgba(255,250,230,.95) 0%,rgba(255,214,150,.7) 40%,rgba(255,214,150,0) 100%),
    radial-gradient(ellipse 520px 300px at 50% 38%,rgba(255,235,205,.9) 0%,rgba(255,235,205,0) 100%),
    linear-gradient(180deg,#fbe7d6 0%,#f6c79e 40%,#e98a4e 72%,#c4532a 100%)}
.brand{position:absolute;left:244px;top:0;width:714px;height:117px;
  background:linear-gradient(180deg,#1a55d6 0%,var(--blue-deep) 100%);
  display:flex;align-items:center;justify-content:center;gap:18px;border:3px solid var(--white)}
.brand-dot{width:44px;height:44px;border-radius:50%;background:var(--white)}
.brand-name{font-family:"Merriweather",serif;font-weight:700;font-size:40px;color:var(--white)}
.hero-text{position:absolute;left:100px;width:1000px;top:160px;text-align:center;
  font-family:"Merriweather",serif;font-size:31px;line-height:51px;color:var(--ink)}
.hero-text b{font-weight:900}
.btn{display:inline-flex;align-items:center;justify-content:center;background:var(--red);color:var(--white);
  font-family:"Merriweather",serif;font-weight:700;border-radius:32px;text-decoration:none}
.hero .btn{position:absolute;left:502px;top:372px;width:196px;height:60px;font-size:21px}

.nav{position:absolute;left:0;top:596px;width:1200px;height:67px;background:var(--red);
  display:flex;justify-content:center;align-items:center;gap:80px}
.nav a{color:var(--white);font-family:"Merriweather",serif;font-weight:700;font-size:15px;text-decoration:none}
.nav a.current{text-decoration:underline}

.section-title{font-family:"Merriweather",serif;font-weight:900;font-size:32px;color:var(--ink);text-align:center}
.section-title span{color:var(--red)}

.what{position:absolute;left:0;top:663px;width:1200px;height:416px;text-align:center;padding-top:40px}
.what .lead{font-family:"Merriweather",serif;font-style:italic;font-size:17px;line-height:31px;width:700px;margin:8px auto 0;color:var(--ink)}
.what h3{font-family:"Merriweather",serif;font-weight:700;font-size:16px;color:var(--ink);margin-top:14px}
.what p.small{font-size:14px;line-height:25px;width:790px;margin:8px auto 0;color:var(--body)}

.band{position:absolute;left:0;width:1200px;display:flex;align-items:center;justify-content:center;text-align:center;
  font-family:"Merriweather",serif;font-weight:700;font-size:36px;line-height:62px;color:var(--white)}
.band-blue{top:1079px;height:385px;background:radial-gradient(ellipse at 50% 50%,#1f6af0 0%,var(--blue) 45%,#0a3bc9 100%)}
.band-red{top:2644px;height:386px;background:radial-gradient(ellipse at 50% 40%,#ff4a1a 0%,var(--red) 50%,#d81a00 100%)}

.photo{position:absolute;left:0;width:1200px}
.photo-church{top:1464px;height:578px;
  background:
    radial-gradient(ellipse 260px 220px at 50% 28%,rgba(255,252,240,.95) 0%,rgba(255,252,240,0) 100%),
    radial-gradient(ellipse 300px 160px at 50% 62%,rgba(196,150,110,.55) 0%,rgba(196,150,110,0) 100%),
    linear-gradient(90deg,rgba(120,95,70,.35) 0%,rgba(120,95,70,0) 22%,rgba(120,95,70,0) 78%,rgba(120,95,70,.35) 100%),
    linear-gradient(180deg,#efe9df 0%,#e2d6c2 38%,#b79a7a 58%,#7a5638 78%,#4a2c1b 100%)}
.photo-crowd{top:3030px;height:577px;
  background:
    radial-gradient(ellipse 200px 160px at 62% 22%,rgba(235,232,228,.85) 0%,rgba(235,232,228,0) 100%),
    radial-gradient(ellipse 160px 110px at 12% 18%,rgba(90,140,130,.6) 0%,rgba(90,140,130,0) 100%),
    radial-gradient(ellipse 240px 140px at 30% 55%,rgba(170,110,80,.45) 0%,rgba(170,110,80,0) 100%),
    radial-gradient(ellipse 260px 150px at 80% 60%,rgba(140,120,110,.5) 0%,rgba(140,120,110,0) 100%),
    linear-gradient(180deg,#5b5450 0%,#6e625b 40%,#3e3532 75%,#221d1b 100%)}

.bio{position:absolute;left:0;top:2042px;width:1200px;height:602px}
.bio .section-title{position:absolute;left:0;width:1200px;top:38px;font-size:32px}
.bio-photo{position:absolute;left:126px;top:100px;width:199px;height:438px;
  background:
    radial-gradient(ellipse 70px 200px at 50% 55%,rgba(40,32,32,.85) 0%,rgba(40,32,32,.4) 60%,rgba(40,32,32,0) 100%),
    radial-gradient(ellipse 40px 50px at 52% 12%,rgba(214,160,130,.8) 0%,rgba(214,160,130,0) 100%),
    #ffffff}
.bio-text{position:absolute;left:416px;top:98px;width:674px;font-size:15.5px;line-height:31px;text-align:justify;color:var(--body)}
.bio-text p+p{margin-top:31px}
.bio .btn{position:absolute;left:417px;top:478px;width:196px;height:63px;font-size:20px}

.team{position:absolute;left:0;top:3607px;width:1200px;height:446px}
.team .section-title{position:absolute;top:50px;width:1200px;font-size:32px}
.member{position:absolute;top:102px;width:280px;height:280px;border-radius:50%;overflow:hidden;border:3px solid var(--red)}
.member.alt{border-color:var(--blue)}
.member .face{position:absolute;inset:0;
  background:radial-gradient(ellipse 90px 110px at 50% 42%,#d9a98c 0%,rgba(217,169,140,0) 100%),linear-gradient(180deg,#f5f3f1 0%,#e4dfdb 100%)}
.member.alt .face{background:radial-gradient(ellipse 90px 110px at 50% 40%,#e8b898 0%,rgba(232,184,152,0) 100%),radial-gradient(ellipse 150px 80px at 50% 95%,#5b2fb0 0%,rgba(91,47,176,0) 100%),linear-gradient(180deg,#ffffff 0%,#eeeeee 100%)}
.member.dark .face{background:radial-gradient(ellipse 90px 110px at 50% 42%,#bdbdbd 0%,rgba(189,189,189,0) 100%),linear-gradient(180deg,#161616 0%,#262626 100%)}
.member .tag{position:absolute;left:0;right:0;bottom:0;height:82px;background:var(--red);text-align:center;padding-top:16px;color:var(--white)}
.member.alt .tag{background:var(--blue)}
.member .tag b{display:block;font-family:"Merriweather",serif;font-size:18px}
.member .tag small{font-size:11px;letter-spacing:1.5px;font-weight:700}
.arrow{position:absolute;top:3832px;width:28px;height:28px}

.footer{position:absolute;left:0;top:4053px;width:1200px;height:605px;background:var(--footer);color:var(--white)}
.field{position:absolute;top:76px;width:224px;height:66px;border:1.5px solid #d9d9d9;border-radius:8px;
  font-size:14px;font-weight:700;padding:0 18px;display:flex;align-items:center}
.submit{position:absolute;left:864px;top:76px;width:224px;height:66px;background:var(--blue);border-radius:8px;
  display:flex;align-items:center;justify-content:center;font-size:20px;font-weight:700}
.rule{position:absolute;left:112px;width:976px;height:1px;background:#555}
.foot-brand{position:absolute;left:112px;top:269px;width:493px;height:87px;background:linear-gradient(180deg,#1a55d6 0%,var(--blue-deep) 100%);border:3px solid var(--white);
  display:flex;align-items:center;justify-content:center;gap:14px}
.foot-brand .brand-dot{width:32px;height:32px}
.foot-brand .brand-name{font-size:30px}
.links{position:absolute;top:272px}
.links h4{font-family:"Merriweather",serif;font-size:21px;font-weight:400;margin-bottom:14px}
.links li{list-style:none;font-size:14px;line-height:34px;display:flex;align-items:center;gap:14px}
.links svg{width:13px;height:13px}
.copyright{position:absolute;top:553px;width:1200px;text-align:center;font-family:"Merriweather",serif;font-size:15px}
</style>
</head>
<body>

<header class="hero" role="img" aria-label="Raised hands silhouetted against a glowing sunset sky with birds">
  <div class="brand"><span class="brand-dot"></span><span class="brand-name">Lanternfold Ministries</span></div>
  <p class="hero-text">Lanternfold Ministries brings the <b>Gospel of Jesus Christ</b>, with<br><b>heart-seeking, biblical accuracy</b><br>through <b>live</b>, <b>entertainment-based</b> evangelistic<br><b>Celebrations</b></p>
  <a class="btn" href="#">Get Started</a>
</header>

<nav class="nav">
  <a class="current" href="#">Home</a>
  <a href="#">Shows &amp; Skylark</a>
  <a href="#">About Lanternfold</a>
  <a href="#">Media</a>
  <a href="#">Contact &amp; Support</a>
</nav>

<section class="what">
  <h2 class="section-title">What <span>we Do</span></h2>
  <p class="lead">In one word, Lanternfold Ministries is about evangelism.  More specifically, evangelism that can be shared, taught and multiplied.</p>
  <h3>This ministry is absolutely committed to:</h3>
  <p class="small">Leading people who are lost, to salvation through Jesus ChristHelping people who are not certain about going to heaven, to be sure...for sureAssisting those who are sure, to “get right” and “stay tight” with God</p>
  <h3 style="margin-top:24px">Lanternfold Ministries continues to:</h3>
  <p class="small">Pioneer evangelistic events through live, entertainment-based, Celebrations.Put into action, real time, real-life research and education developmentMultiply every evangelistic method and effort so each can be taught, learned, shared and duplicated. Innovate cutting-edge methods to share the Gospel so it can be clearly understood and responded to</p>
</section>

<section class="band band-blue">
  <p>Reuben Ashcombe is a Christian Illusionist, Musician,<br>Author, and a very Funny Guy.<br>He’s also a five-star rated Skylark SportsTM<br>Entertainer and Speaker!</p>
</section>

<div class="photo photo-church" role="img" aria-label="Congregation seated in pews facing the altar of an ornate church"></div>

<section class="bio">
  <h2 class="section-title">Reuben <span>Ashcombe</span></h2>
  <div class="bio-photo" role="img" aria-label="Portrait of Reuben Ashcombe seated on a director's chair"></div>
  <div class="bio-text">
    <p>Reuben Ashcombe began appearing professionally when he was just thirteen years of age. By sixteen, Ashcombe had embarked on a journey that would soon rocket him to the stages of hotels, theaters and luxury cruise ships worldwide. By twenty he had established himself as a truly international, master in the art of theatrical stage illusion. In his thirties, Ashcombe became a sought after entertainer and speaker for top corporations.</p>
    <p>Little did he know, his most important work was yet to reveal itself. In the midst of the bright lights of Las Vegas, Ashcombe felt a tug on his heart. As he struggled to understand, it soon became clear; God had other plans. God was calling Ashcombe to service, to a life of change and a commission with an eternal promise.Today Reuben Ashcombe shares his God-given talents along with the energy and candor of his faith, in each “Lanternfold It!”... Celebration of Wonder.</p>
  </div>
  <a class="btn" href="#">Read More</a>
</section>

<section class="band band-red">
  <p>Reuben is a member of The Guild of Stage Illusionists,<br>The Circle of Gospel Conjurers<br>and is a ridiculed member of<br>Ironleaf Gym.</p>
</section>

<div class="photo photo-crowd" role="img" aria-label="Worshipper raising a hand above a blurred crowd at a live event"></div>

<section class="team">
  <h2 class="section-title">Our <span>Team</span></h2>
  <div class="member" style="left:110px">
    <div class="face" role="img" aria-label="Portrait of Reuben Ashcombe"></div>
    <div class="tag"><b>Reuben Ashcombe</b><small>PRESIDENT</small></div>
  </div>
  <div class="member alt" style="left:460px">
    <div class="face" role="img" aria-label="Portrait of Marla Fenwick"></div>
    <div class="tag"><b>Marla Fenwick</b><small>SECRETARY TREASURER</small></div>
  </div>
  <div class="member dark" style="left:809px">
    <div class="face" role="img" aria-label="Portrait of Tobias Wren"></div>
    <div class="tag"><b>Tobias Wren</b><small>DIRECTOR</small></div>
  </div>
</section>
<svg class="arrow" style="left:35px" viewBox="0 0 28 28"><circle cx="14" cy="14" r="14" fill="#111"/><path d="M16 8l-6 6 6 6" stroke="#fff" stroke-width="2.6" fill="none"/></svg>
<svg class="arrow" style="left:1132px" viewBox="0 0 28 28"><circle cx="14" cy="14" r="14" fill="#111"/><path d="M12 8l6 6-6 6" stroke="#fff" stroke-width="2.6" fill="none"/></svg>

<footer class="footer">
  <div class="field" style="left:112px">Name</div>
  <div class="field" style="left:363px">Email</div>
  <div class="field" style="left:613px">Phone</div>
  <div class="submit">Submit</div>
  <div class="rule" style="top:196px"></div>
  <div class="foot-brand"><span class="brand-dot"></span><span class="brand-name">Lanternfold Ministries</span></div>
  <div class="links" style="left:663px">
    <h4>Quick Links</h4>
    <ul>
      <li><svg viewBox="0 0 14 14"><path d="M1 7h11M7 2l5 5-5 5" stroke="#fff" stroke-width="2.2" fill="none"/></svg>Home</li>
      <li><svg viewBox="0 0 14 14"><path d="M1 7h11M7 2l5 5-5 5" stroke="#fff" stroke-width="2.2" fill="none"/></svg>About Lanternfold</li>
      <li><svg viewBox="0 0 14 14"><path d="M1 7h11M7 2l5 5-5 5" stroke="#fff" stroke-width="2.2" fill="none"/></svg>Shows &amp; Skylark</li>
      <li><svg viewBox="0 0 14 14"><path d="M1 7h11M7 2l5 5-5 5" stroke="#fff" stroke-width="2.2" fill="none"/></svg>Latest News</li>
      <li><svg viewBox="0 0 14 14"><path d="M1 7h11M7 2l5 5-5 5" stroke="#fff" stroke-width="2.2" fill="none"/></svg>Contact &amp; Support</li>
    </ul>
  </div>
  <div class="links" style="left:896px">
    <h4>Help Links</h4>
    <ul>
      <li><svg viewBox="0 0 14 14"><path d="M1 7h11M7 2l5 5-5 5" stroke="#fff" stroke-width="2.2" fill="none"/></svg>FAQ</li>
      <li><svg viewBox="0 0 14 14"><path d="M1 7h11M7 2l5 5-5 5" stroke="#fff" stroke-width="2.2" fill="none"/></svg>Terms of use</li>
      <li><svg viewBox="0 0 14 14"><path d="M1 7h11M7 2l5 5-5 5" stroke="#fff" stroke-width="2.2" fill="none"/></svg>Privacy Policy</li>
      <li><svg viewBox="0 0 14 14"><path d="M1 7h11M7 2l5 5-5 5" stroke="#fff" stroke-width="2.2" fill="none"/></svg>Support Links</li>
      <li><svg viewBox="0 0 14 14"><path d="M1 7h11M7 2l5 5-5 5" stroke="#fff" stroke-width="2.2" fill="none"/></svg>Conditions</li>
    </ul>
  </div>
  <div class="rule" style="top:524px"></div>
  <p class="copyright">Copyright © 2023.Lanternfold Ministries Inc. All Rights Reserved.</p>
</footer>

</body>
</html>
```